Three Ebook Covers for Short Stories

Three Ebook cover designs for 3 short stories (all linked) psychological thriller. I like clean crisp images. Perhaps with an imagine of eyes/part of face - white woman, 29, thin, brown eyes, short bob hair. I like gritty, moody, raw type of images. I dont mind the same image being used on three covers providing there are differences (ie slight variation in colour of book). Colours I prefer red, burgundy, black, grey, white. My website shows off the type of colours I prefer. www.lydiakbarnes-author.net
Branding is important.

Target Market(s)

Adult. Moth in Attic, Lost Field, type of readers.

Industry/Entity Type

Book Publisher

Font styles to use
Sans Serif
Other font styles liked:
• fonts used on thriller novels

Requirements
Must have
• Author Name: Lydia K Barnes
• Short Story as Part of Title
• Short Story 1: Title - First Crow
• Short Story 2: Title - Second Crow
• Short Story 3: Title - Third Crow
• Branding is important so they must look like they are a set.
• A font which is aligned to thriller type novels
• Colours aligned to my website - red, burgundy, white, grey, black.
Nice to have
• I don't mind a black and white type photo imagine.
Should not have
• n/a

```html
<!DOCTYPE html>
<html lang="en">
<head>
<meta charset="utf-8">
<title>First Crow — Lydia K Barnes</title>
<link rel="stylesheet" href="https://fonts.googleapis.com/css2?family=Russo+One&family=Oswald:wght@500;700&display=swap">
<style>
  :root {
    --fog-top: #cfd0c6;
    --fog-mid: #8e9088;
    --fog-low: #4a4c47;
    --fog-bottom: #262824;
    --burgundy: #5c1a1d;
    --paper: #f4f1ee;
    --eye-light: #e27a9a;
    --eye-mid: #b8304f;
    --eye-dark: #6e1228;
    --author-grey: #c9c7bd;
    --series-ink: #2a2a28;
  }
  html, body {
    margin: 0;
    padding: 0;
    width: 1106px;
    height: 1200px;
    overflow: hidden;
    background: #ffffff;
  }
  .cover {
    position: relative;
    width: 1106px;
    height: 1200px;
    overflow: hidden;
  }
  .cover__backdrop {
    position: absolute;
    inset: 0;
    background:
      radial-gradient(ellipse at 78% 55%, rgba(40,42,38,0.35), rgba(40,42,38,0) 55%),
      linear-gradient(180deg, var(--fog-top) 0%, var(--fog-mid) 45%, var(--fog-low) 72%, var(--fog-bottom) 100%);
  }
  .cover__series-number {
    position: absolute;
    left: 14px;
    top: 10px;
    margin: 0;
    font-family: "Oswald", sans-serif;
    font-weight: 700;
    font-size: 26px;
    color: var(--series-ink);
  }
  .cover__torn-strip {
    position: absolute;
    left: 0;
    top: 170px;
    width: 1106px;
    height: 250px;
  }
  .cover__title {
    position: absolute;
    left: 0;
    top: 420px;
    margin: 0;
    font-family: "Russo One", sans-serif;
    font-weight: 400;
    color: var(--burgundy);
    font-size: 96px;
    line-height: 96px;
    letter-spacing: 14px;
  }
  .cover__title-line { display: block; white-space: nowrap; }
  .cover__title-line--first { padding-left: 6px; }
  .cover__title-line--second { padding-left: 290px; }
  .cover__author {
    position: absolute;
    right: 10px;
    bottom: 28px;
    margin: 0;
    font-family: "Oswald", sans-serif;
    font-weight: 500;
    font-size: 36px;
    letter-spacing: 6px;
    font-variant: small-caps;
    color: var(--author-grey);
  }
</style>
</head>
<body>
  <main class="cover">
    <div class="cover__backdrop" role="img" aria-label="Grey black-and-white photo of a misty forest fading to darkness"></div>

    <p class="cover__series-number">1.</p>

    <svg class="cover__torn-strip" viewBox="0 0 1106 250" role="img" aria-label="Red-tinted close-up photo of a woman's eyes seen through a tear in paper">
      <defs>
        <linearGradient id="eyeTone" x1="0" y1="0" x2="1" y2="0">
          <stop offset="0" stop-color="var(--eye-mid)"/>
          <stop offset="0.45" stop-color="var(--eye-light)"/>
          <stop offset="0.7" stop-color="var(--eye-mid)"/>
          <stop offset="1" stop-color="var(--eye-dark)"/>
        </linearGradient>
      </defs>
      <path class="torn-strip__paper" fill="var(--paper)"
        d="M0 58 L40 52 L90 60 L150 48 L210 50 L260 40 L330 44 L400 36 L470 42 L540 30 L600 26 L650 14 L690 20 L740 10 L790 18 L850 12 L910 22 L980 16 L1040 26 L1106 22
           L1106 210 L1050 204 L990 214 L930 208 L870 220 L800 226 L740 234 L690 226 L640 236 L580 242 L520 236 L460 240 L400 232 L340 238 L280 230 L220 236 L160 228 L100 232 L40 222 L0 226 Z"/>
      <path class="torn-strip__image" fill="url(#eyeTone)"
        d="M0 68 L45 62 L95 70 L150 58 L215 60 L265 50 L330 54 L400 46 L470 52 L540 40 L600 36 L650 24 L690 32 L740 22 L790 30 L850 24 L910 34 L980 28 L1040 38 L1106 34
           L1106 198 L1050 194 L990 202 L930 198 L870 208 L800 214 L740 222 L690 214 L640 224 L580 230 L520 224 L460 228 L400 220 L340 226 L280 218 L220 224 L160 216 L100 220 L40 212 L0 214 Z"/>
    </svg>

    <h1 class="cover__title">
      <span class="cover__title-line cover__title-line--first">FIRST</span>
      <span class="cover__title-line cover__title-line--second">CROW</span>
    </h1>

    <p class="cover__author">Lydia K Barnes</p>
  </main>
</body>
</html>
```